Workforce Placement Agency - Bridges to Careerhood!

Workforce Placement Agency – Bridges to Careerhood
A Company with a point of difference!

http://www.mywpx.com.au/

Please find the following 17 attached files to complete this project with no confusion.

The brochure should have 3 folds with information front and back!

- 4 logo design attachments (use coloured ones only - NOT black and white)
- 2 pages of brochure layout
- Contact Information (Front page with logo, summary of services - also attached)
- Who We Are
- Vacant Positions (Jobs)
- Mentoring Services for Employees
- Recruitment Services for the Employer (including Other Services)
- Business and Management Maintenance
- Employability Skilling Service (Courses)
- What We Offer
- Business Start-up

THESE SHOULD BE ALL JUSTIFIED!

All services are provided on a fee for services bases – costs are charged out in line with the specific service delivered and the staff qualifications required to deliver the service!

Please review my website for my company colours and further information on my services and location.

Reason: No adequate designs that meet all com pay specifications - but they are improving!

Please review the change of specifications to hopefully make your job MUCH more earlier!

I look forward to your update!

Thank you for your time!

Kindest regards, Clara.

Reason: No designs to specifications to date! I have updated specifications to hopefully make the designers job easier! Thank you Clara.

Good evening,

This project is now becoming very urgent - I look forward to hopefully seeing your designs soon!

Thank you, Clara.

Target Market(s)

- People wanting to start up a new business in Australia
- People needing professional bookkeeping services in Australia
- Employers needing staff in all industries
- Local and international (migrants) Employees wanting to find work
- All job seekers through out Australia
- Migrants requiring coaching services helping them to find employment in Australia
- People wanting to up-skill and attend training courses

Industry/Entity Type

Business

Requirements
Must have
• Use purple and yellow logo and colours in attached vector file to match my website.
Should not have
• No not use black and white logos in attached vector files

```html
<!DOCTYPE html>
<html lang="en">
<head>
<meta charset="utf-8">
<title>Workforce Placement Agency – Services Brochure (Inside)</title>
<link rel="stylesheet" href="https://fonts.googleapis.com/css2?family=PT+Sans:ital,wght@0,400;0,700;1,700&display=swap">
<style>
  :root {
    --purple-deep: #24134f;
    --purple-mid: #3a2577;
    --purple-glow: #5a48a0;
    --divider: #160a36;
    --yellow: #f6b70f;
    --leaf: #f3c21a;
    --ink: #241632;
    --white: #ffffff;
  }
  * { margin: 0; padding: 0; box-sizing: border-box; }
  html, body { width: 1200px; height: 844px; overflow: hidden; }
  body {
    font-family: "PT Sans", Arial, sans-serif;
    background: var(--purple-deep);
  }
  .brochure {
    position: relative;
    width: 1200px;
    height: 844px;
    background:
      radial-gradient(ellipse 420px 520px at 600px 460px, var(--purple-glow) 0%, transparent 70%),
      radial-gradient(ellipse 380px 480px at 1000px 520px, #4a3890 0%, transparent 70%),
      radial-gradient(ellipse 320px 420px at 200px 560px, #43318a 0%, transparent 70%),
      linear-gradient(180deg, var(--purple-mid), var(--purple-deep));
    overflow: hidden;
  }
  .divider {
    position: absolute; top: 0; width: 4px; height: 844px;
    background: var(--divider);
  }
  .leaf {
    position: absolute;
    border-radius: 50%;
    background: radial-gradient(circle, var(--leaf) 0%, #e0a30c 70%, rgba(224,163,12,0) 72%);
    opacity: .9;
  }
  .section-title {
    position: absolute;
    color: var(--white);
    font-weight: 700;
    font-size: 17px;
    letter-spacing: .1px;
    white-space: nowrap;
  }
  .section-title.large { font-size: 19px; }
  .panel {
    position: absolute;
    background: var(--yellow);
    color: var(--ink);
    font-weight: 700;
    font-size: 11px;
    line-height: var(--lh, 14px);
    padding: 7px 10px 6px 12px;
    text-align: justify;
    overflow: hidden;
  }
  .panel p { margin-bottom: 2px; }
  .panel ul { list-style: none; }
  .panel li { position: relative; padding-left: 11px; }
  .panel li::before {
    content: ""; position: absolute; left: 1px; top: calc(var(--lh, 14px) / 2 - 2px);
    width: 4px; height: 4px; border-radius: 50%; background: var(--white);
  }
  .panel .sub { color: var(--white); padding-left: 11px; }
  .panel .label { color: var(--white); }
  .note {
    position: absolute;
    color: var(--white);
    font-weight: 700;
    font-style: italic;
    font-size: 10.5px;
    line-height: 13px;
  }
</style>
</head>
<body>
<main class="brochure">
  <div class="divider" style="left:398px"></div>
  <div class="divider" style="left:798px"></div>

  <div class="leaf" role="img" aria-label="Yellow maple leaf illustration" style="left:150px;top:2px;width:50px;height:42px"></div>
  <div class="leaf" role="img" aria-label="Yellow maple leaf illustration" style="left:322px;top:394px;width:60px;height:56px"></div>
  <div class="leaf" role="img" aria-label="Yellow maple leaf illustration" style="left:745px;top:417px;width:44px;height:42px"></div>
  <div class="leaf" role="img" aria-label="Yellow maple leaf illustration" style="left:1160px;top:376px;width:34px;height:34px"></div>

  <!-- Column 1 -->
  <h2 class="section-title" style="left:12px;top:18px">What we offer</h2>
  <section class="panel" style="left:12px;top:52px;width:382px;height:293px;--lh:15.2px">
    <p>Our company provides transparent, accurate, reliable and quality services while also demonstrating model, ethical behaviour and leadership in the areas of:</p>
    <ul>
      <li>Assisting people through the process of starting up and managing their own business in Australia;</li>
      <li>Mentoring Employees with diverse skills to approach and secure employment in the Australian Workforce across ALL Employment sectors, which include, but are not limited to: Trades, Professional Services, and other Labour Industries such as, Hospitality and Tourism;</li>
      <li>All Services are customised to suit individual requirements of both the employer and employee;</li>
      <li>Match Employers with the appropriate Employee from both local and International labour-force;</li>
      <li>Specialised mentoring services to migrant workers seeking employment within Australia, assisting employers to access this unique but under-utilised workforce; and</li>
      <li>Our service area is throughout ALL of Australia including remote and regional areas.</li>
    </ul>
  </section>
  <p class="note" style="left:6px;top:352px;width:390px">We supply our services in a comprehensive and cost competitive manner, while providing our individual customer care advantage!</p>

  <h2 class="section-title" style="left:12px;top:423px">Business Start-up</h2>
  <section class="panel" style="left:12px;top:472px;width:382px;height:367px;--lh:14.9px">
    <ul>
      <li>Decide what business structure is right for you</li>
      <li>Company and Business Name Search</li>
      <li>Understanding legal obligations</li>
      <li>Obtain consent from officers and members (if required)</li>
      <li>Negotiate Shareholdings (if required)</li>
      <li>Register Companies, Trading Names and other Entities</li>
      <li>Signing Company Registers</li>
      <li>Explanations of Company Members and Shareholders responsibilities when signing Company Registers</li>
      <li>Direction on Trade Marking Your Business</li>
      <li>Decide if cash or accrual accounting is appropriate for your business</li>
      <li>Tax File Number (TFN) Registration</li>
      <li>Australian Business Number (ABN) Registration</li>
      <li>Goods and Services (GST) registration (if required)</li>
      <li>Pay as you earn (PAYE) tax (if required)</li>
      <li>Fuel Tax Credits Registration (if required)</li>
      <li>Fringe Benefits Tax (FBT) Registration (if required)</li>
      <li>Luxury Car Tax Registration (if required)</li>
      <li>Superannuation Obligations</li>
      <li>Workers Compensation and/or Personal Accident and illness insurance information (contingent on your Business structure)</li>
    </ul>
  </section>

  <!-- Column 2 -->
  <h2 class="section-title" style="left:410px;top:15px">Business Management &amp; Maintenance</h2>
  <section class="panel" style="left:406px;top:49px;width:388px;height:363px;--lh:13.3px">
    <ul>
      <li>Help clients understand their obligations</li>
      <li>Assist clients to manage legislative requirements for BAS and a financial year</li>
      <li>Educate clients on how money flows through a business</li>
      <li>Professional bookkeeping duties ensuring high-quality business records are kept</li>
      <li>LedgerPro set-up to record, maintain and report your business accounts</li>
    </ul>
    <p class="sub">- Clients DO NOT have to purchase and upgrade accounting Software</p>
    <ul>
      <li>Data entry into LedgerPro</li>
      <li>Recording vehicle expenses</li>
      <li>Petty cash systems</li>
      <li>Payroll management:</li>
    </ul>
    <p class="sub">- Declarations - Payment records - Annual records - Superannuation records - Fringe benefits provided by you</p>
    <ul>
      <li>Debtor and Creditor management</li>
      <li>Reconcile business accounts:</li>
    </ul>
    <p class="sub">- Bank accounts - Loan Accounts - Sales register - Purchase register - Inventory - Jobs - Payroll - Superannuation Obligations</p>
    <ul>
      <li>Timely financial reporting to internal and external stake holders (tailored to your business requirements)</li>
      <li>Prepare information for you to complete your Business activity Statement (BAS) in a timely manner ready for you to submit to the Australian Taxation Office (ATO) and helping you to avoid any fines penalties, fees and charges!</li>
    </ul>
  </section>

  <h2 class="section-title" style="left:424px;top:429px">Employability Skilling Service (Courses)</h2>
  <section class="panel" style="left:406px;top:464px;width:388px;height:320px;--lh:12.6px">
    <p class="label">Skills to find employment courses:</p>
    <ul>
      <li>Writing Job Applications</li>
      <li>The Purpose and how to write a Cover Letter</li>
      <li>The Purpose and how to write a Resume</li>
      <li>Interview Skills and techniques</li>
      <li>Employability Skills</li>
      <li>Job Hunting Methods</li>
      <li>Graduate Recruitment</li>
      <li>Part-time and Casual Work (Differences)</li>
      <li>Preparation to find work in Australia as an International Student</li>
      <li>Seminar on working overseas and differences in Australia</li>
    </ul>
    <p class="label">Other Courses include:</p>
    <ul>
      <li>Servicing persons through the process of Starting up your own Business in Australia</li>
      <li>Your Company and the law</li>
      <li>Financial Services (Bookkeeping)</li>
      <li>Frontline Management</li>
      <li>Project Management</li>
      <li>Implementation of emergency procedures (OH&amp;S)</li>
      <li>Learn English</li>
      <li>Learn Mandarin</li>
      <li>Learn Cantonese</li>
    </ul>
  </section>
  <p class="note" style="left:410px;top:796px;width:384px">All course modules are available for us to work together to design a unique course that can be tailored to suit your company and industry requirements!</p>

  <!-- Column 3 -->
  <h2 class="section-title" style="left:814px;top:10px">Employee Mentoring Services:</h2>
  <section class="panel" style="left:808px;top:41px;width:388px;height:313px;--lh:13.4px">
    <ul>
      <li>Provide access to employment opportunities, encompassing ALL Australian Industry sectors</li>
      <li>Provide access to employment opportunities throughout ALL of Australia including remote and regional areas</li>
      <li>Match Employees with the appropriate Employers from both Local and International labour-force</li>
      <li>Specialised Mentoring services for International and Local Students seeking Employment in the Australian workforce</li>
      <li>Career Training Services for Migrants including: Interview Skills and Techniques, Employability Skills and the Australian Business Culture</li>
      <li>Career Mentoring Services for our Local and Indigenous community including: Interview Skills and Techniques and Employability Skills</li>
      <li>Uniquely designed Cover Letters and Resumes tailored to positions</li>
      <li>Uniquely designed Selection Criteria Job Applications</li>
      <li>Job Hunting Methods</li>
      <li>Provide employee access to experts requiring skills Assessments</li>
      <li>Provide employee access to experts seeking apprenticeships and traineeships</li>
      <li>Career counselling</li>
      <li>Access to language schools</li>
      <li>Prepare International and Local employees with skills to sell themselves to future employers</li>
    </ul>
  </section>
  <p class="note" style="left:806px;top:359px;width:392px;font-size:9.6px">Mentoring services are provided individually (uniquely tailored) or in group sessions!</p>

  <h2 class="section-title large" style="left:830px;top:381px">Recruitment Services for the Employer</h2>
  <section class="panel" style="left:808px;top:414px;width:388px;height:425px;--lh:12.4px">
    <p class="label">Core Services:</p>
    <ul>
      <li>Service ALL Employment industries</li>
      <li>Match Employers with the appropriate Employee from both Local and International Labour-force</li>
      <li>Advise for employers of their ability and benefits to employing persons from overseas</li>
      <li>Our service area is throughout ALL of Australia including, remote and regional areas</li>
      <li>Provide employer access to experts requiring skills assessments for employees</li>
      <li>Provide employer access to experts seeking apprentices and trainees</li>
      <li>Discuss the position specification and company expectation of the potential candidate</li>
      <li>Job descriptions</li>
      <li>Database Searches</li>
      <li>Appropriate advertising campaign (inc. Preparation and Responses in consultation with employer)</li>
      <li>Telephone Screening and Short listing Candidates</li>
      <li>Interview candidates</li>
      <li>Reference Checking (inc. Qualification Checks)</li>
      <li>Referee Reports</li>
      <li>Advising Successful and Unsuccessful Candidates</li>
    </ul>
    <p class="label">Other Services:</p>
    <ul>
      <li>Skills Testing</li>
      <li>Psychological Services such as psychometric testing and profiling</li>
      <li>Advertising such as newspapers, display, flyers, industry magazines and executive position advertising.</li>
      <li>Executive and search recruitment services will attract specific terms and conditions, as outlined in our Executive/Search Services Policy</li>
      <li>Professional bookkeeping and payroll services</li>
      <li>Workplace conflict resolution</li>
      <li>Participating on interview panels and interview Reports</li>
    </ul>
  </section>
</main>
</body>
</html>
```